Spider vein removal and more postcard design

Harborview Skin Clinic located on West Callowmere Rd in Jupiter, FL directly across the street from the Brightwell Drake Playhouse (the old Lyle Osterman theatre) specializes in spider-vein removal using the latest evidence-based guidelines and FDA-approved medications at the lowest cost in the Tri-County area! We also provide Smoothra, Kalivane, and the only FDA-approved medication for cheeks - Pellora!!! We provide excellence in esthetics and the ultimate in patient service! Call about our new patient specials...(561) 555-0143 or visit our website: HarborviewSkinClinic.example

```html
<!DOCTYPE html>
<html lang="en">
<head>
<meta charset="utf-8">
<title>Harborview Skin Clinic Postcard</title>
<link rel="stylesheet" href="https://fonts.googleapis.com/css2?family=Questrial&family=Arimo:wght@400;700&family=Oswald:wght@500;600&family=Allura&family=Great+Vibes&family=Marcellus&family=Playfair+Display:wght@400&display=swap">
<style>
:root{
  --page:#151716;
  --teal:#93cdc5;
  --teal-deep:#6fb5ab;
  --gold:#d9bb8c;
  --gold-light:#ecdcbf;
  --ink:#2b2b2b;
  --white:#ffffff;
  --orange:#d9822b;
  --navy:#0f2d42;
  --rule:#c9c9c9;
}
*{margin:0;padding:0;box-sizing:border-box}
html,body{width:1100px;height:1200px;overflow:hidden;background:var(--page)}
body{position:relative;font-family:"Arimo",Arial,sans-serif;color:var(--ink)}
.card{position:absolute;left:125px;width:864px;height:558px;background:var(--white);overflow:hidden}
.card--front{top:32px}
.card--back{top:615px}
.card svg.backdrop{position:absolute;inset:0}
.abs{position:absolute;white-space:nowrap}
.wrap{white-space:normal}
.brand{position:absolute;text-align:center;width:330px}
.brand__mark{display:block;margin:0 auto;width:58px;height:58px;border-radius:50%;background:var(--gold);border:3px solid var(--gold-light)}
.brand__name{font-family:"Questrial",sans-serif;font-size:20px;color:var(--white);letter-spacing:1px;margin-top:8px;padding-bottom:5px;border-bottom:1px solid var(--white)}
.headline__lead{left:90px;top:134px;font-family:"Questrial",sans-serif;font-size:17px;line-height:20px;color:var(--white)}
.headline__script{left:212px;top:104px;font-family:"Allura",cursive;font-size:64px;line-height:70px;color:var(--gold-light)}
.headline__tail{left:220px;top:180px;font-family:"Questrial",sans-serif;font-size:17px;line-height:20px;color:var(--white);letter-spacing:.5px}
.intro{left:28px;top:226px;width:440px;text-align:center;font-size:13px;line-height:16.5px;color:var(--ink)}
.divider{left:110px;top:316px;width:280px;border-top:1px solid var(--white)}
.call{left:0;top:324px;width:500px;text-align:center;font-family:"Oswald",sans-serif;font-weight:600;font-size:33px;line-height:38px;color:var(--ink);letter-spacing:-.5px}
.call span{color:var(--white)}
.email-line{left:0;top:364px;width:500px;text-align:center;font-size:16px;line-height:20px;color:var(--ink)}
.address{left:35px;top:468px;font-family:"Questrial",sans-serif;font-size:16px;line-height:20.5px;color:#111;font-style:normal}
.directions{left:339px;top:476px;width:320px;text-align:center;font-size:13.5px;line-height:16.5px;color:var(--orange)}
.label{font-size:13px;color:#111;text-align:center;line-height:14px}
.website{right:36px;top:29px;font-size:16px;color:#111}
.photo{position:absolute}
.stamp{left:753px;top:28px;width:73px;height:84px;border:1px solid var(--rule);color:#9a9a9a;font-size:13px;line-height:17px;padding:19px 0 0 18px}
.consult{left:390px;top:19px;width:271px;height:79px}
.consult__text{position:absolute;left:0;top:12px;width:100%;text-align:center;color:var(--white);font-family:"Questrial",sans-serif;font-size:17px;line-height:19px}
.consult__text b{font-family:"Arimo",sans-serif;font-weight:700;font-size:16px;letter-spacing:.5px}
.hours{left:397px;top:107px;width:280px;text-align:center;font-size:13px;line-height:14px;color:var(--white)}
.tagline{left:37px;top:141px;font-size:17px;color:var(--white)}
.about{left:37px;top:176px;width:648px;font-size:14px;line-height:16.8px;text-align:justify;color:var(--ink)}
.coupon{left:39px;top:275px;width:292px;height:166px;border:1.5px dashed #555;background:linear-gradient(to bottom,var(--white) 30%,#e0c9a8)}
.coupon__head{position:absolute;left:4px;top:11px;right:4px;height:31px;background:var(--teal);color:var(--white);font-family:"Marcellus",serif;font-size:22px;text-align:center;line-height:31px;letter-spacing:1px}
.coupon__photo{position:absolute;left:6px;top:46px;width:160px;height:88px}
.coupon__small{position:absolute;left:183px;top:54px;width:100px;text-align:center;font-family:"Playfair Display",serif;font-size:10px;line-height:9px;color:#222}
.coupon__price{position:absolute;left:172px;top:58px;font-family:"Playfair Display",serif;font-size:66px;color:#111;line-height:76px}
.coupon__price sup{font-size:28px;vertical-align:top;position:relative;top:8px}
.coupon__foot{position:absolute;left:0;right:0;top:140px;text-align:center;font-family:"Marcellus",serif;font-size:16px;line-height:20px;color:#222;letter-spacing:.5px}
.rid{left:344px;top:261px;font-size:19px;line-height:22px;color:#111}
.rid-script{left:378px;top:282px;font-family:"Great Vibes",cursive;font-size:32px;line-height:36px;color:var(--teal-deep)}
.mail-lines{left:597px;width:229px;border-top:1px solid var(--rule)}
.schedule{left:37px;top:465px;font-size:15px;color:#111;letter-spacing:.3px}
.contact{left:37px;top:495px;font-size:14px;line-height:18px;color:#111}
.scissors{left:30px;top:266px}
</style>
</head>
<body>

<section class="card card--front" aria-label="Postcard front">
  <svg class="backdrop" width="864" height="558" viewBox="0 0 864 558" aria-hidden="true">
    <defs>
      <radialGradient id="beach" cx="70%" cy="25%" r="80%">
        <stop offset="0" stop-color="#fffdf5"/>
        <stop offset=".5" stop-color="#f1dcb1"/>
        <stop offset="1" stop-color="#d8b57e"/>
      </radialGradient>
      <linearGradient id="face" x1="0" y1="0" x2="1" y2="1">
        <stop offset="0" stop-color="#f3e4d8"/>
        <stop offset="1" stop-color="#d9b59b"/>
      </linearGradient>
    </defs>
    <path d="M0 0 H864 V420 C700 420 540 390 400 382 C250 374 120 372 0 378 Z" fill="var(--teal)"/>
    <path d="M0 395 C150 380 300 385 440 400 C600 418 760 470 864 540 V558 C760 500 600 440 440 420 C300 404 150 400 0 420 Z" fill="var(--gold)"/>
    <path d="M0 440 C160 420 320 430 460 450 C300 440 160 440 0 460 Z" fill="var(--gold-light)"/>
    <path d="M420 470 C560 440 720 470 864 500 V512 C720 482 560 458 420 470 Z" fill="var(--gold-light)"/>
  </svg>

  <svg class="photo" style="left:0;top:0" width="864" height="558" viewBox="0 0 864 558">
    <circle cx="710" cy="222" r="226" fill="var(--gold-light)"/>
    <circle cx="710" cy="222" r="222" fill="url(#beach)" role="img" aria-label="Photo: woman relaxing in a hammock on a sunny beach"/>
    <circle cx="576" cy="325" r="94" fill="var(--gold-light)"/>
    <circle cx="576" cy="325" r="90" fill="url(#face)" role="img" aria-label="Photo: injection treatment near the eye"/>
    <circle cx="740" cy="431" r="103" fill="var(--gold-light)"/>
    <circle cx="740" cy="431" r="99" fill="url(#face)" role="img" aria-label="Photo: dermal filler treatment on the forehead"/>
  </svg>

  <div class="abs website">www.harborviewskinclinic.example</div>
  <div class="abs label" style="left:490px;top:170px;width:104px">SPIDER VEIN<br>REMOVAL</div>
  <div class="abs label" style="left:540px;top:394px;width:70px">SMOOTHRA</div>
  <div class="abs label" style="left:680px;top:358px;width:120px">DERMAL FILLERS</div>

  <div class="brand" style="left:88px;top:22px">
    <span class="brand__mark"></span>
    <div class="brand__name">Harborview Skin Clinic</div>
  </div>

  <span class="abs headline__lead">REGAIN YOUR</span>
  <span class="abs headline__script">Youthful</span>
  <span class="abs headline__tail">APPEARANCE TODAY</span>

  <p class="abs wrap intro">Harborview Skin Clinic specializes in spider-vein removal using the latest evidence-based guidelines and FDA-approved medications at the lowest cost in the Tri-County area!<br>We also provide Smoothra, Kalivane, and the only FDA-approved medication for cheeks - Pellora!!!</p>
  <div class="abs divider"></div>
  <div class="abs call">Call Today - <span>561-555-0143</span></div>
  <div class="abs email-line">Email - HarborviewSkin@mail.example</div>

  <address class="abs address">Harborview Skin Clinic<br>1080 West Callowmere Rd, Suite 106B<br>Jupiter, FL 33477</address>
  <p class="abs wrap directions">Finding us is easy! Our office is located directly across the street from the Brightwell Drake Playhouse (the old Lyle Osterman Theatre)</p>
</section>

<section class="card card--back" aria-label="Postcard back">
  <svg class="backdrop" width="864" height="558" viewBox="0 0 864 558" aria-hidden="true">
    <rect x="0" y="0" width="724" height="251" fill="var(--teal)"/>
  </svg>

  <div class="brand" style="left:40px;top:30px">
    <span class="brand__mark"></span>
    <div class="brand__name">Harborview Skin Clinic</div>
  </div>

  <div class="abs consult">
    <svg width="271" height="79" viewBox="0 0 271 79" aria-hidden="true">
      <path d="M0 0 H271 V50 L135 79 L0 50 Z" fill="var(--navy)"/>
    </svg>
    <div class="consult__text">Request a Free<br><b>CONSULTATION</b></div>
  </div>

  <div class="abs hours">Monday to Wednesday: <b>9:30 AM – 6:00 PM</b><br>Thursday to Friday: <b>Closed</b><br>Saturday: <b>9:30 AM – 2:00 PM</b><br>Sunday: <b>Closed</b></div>

  <div class="abs stamp">Place<br>Stamp<br>Here</div>

  <div class="abs tagline">Love Those Legs!</div>
  <p class="abs wrap about">Harborview Skin Clinic in Jupiter, FL, offers a wide range of medical esthetic treatments, including spider vein removal, Smoothra, and dermal fillers. Committed to helping you to look and feel youthful, we provide quality patient care and stellar customer service. Come and visit our beautiful location right across the street from the Atlantic Ocean. You won’t be disappointed!</p>

  <svg class="abs scissors" width="20" height="14" viewBox="0 0 20 14" aria-hidden="true">
    <circle cx="4" cy="3" r="2.5" fill="none" stroke="#222" stroke-width="1.3"/>
    <circle cx="4" cy="11" r="2.5" fill="none" stroke="#222" stroke-width="1.3"/>
    <path d="M6 4 L19 10 M6 10 L19 4" stroke="#222" stroke-width="1.3"/>
  </svg>

  <div class="abs coupon">
    <div class="coupon__head">NEW PATIENT SPECIAL</div>
    <div class="coupon__photo" role="img" aria-label="Photo: row of bare legs" style="background:linear-gradient(to bottom,#f4e7dc,#d8ab8c)"></div>
    <div class="coupon__small">30 SPIDER VEIN<br>TREATMENTS</div>
    <div class="coupon__price"><sup>$</sup>99</div>
    <div class="coupon__foot">CALL FOR MORE INFORMATION</div>
  </div>

  <div class="abs rid">Get Rid Of Those</div>
  <div class="abs rid-script">Spider Viens</div>
  <div class="abs" role="img" aria-label="Photo: smiling woman in glasses pointing to the special offer" style="left:370px;top:322px;width:156px;height:162px;background:linear-gradient(to bottom,#f7f1ec,#b9b7b6)"></div>

  <div class="abs mail-lines" style="top:319px"></div>
  <div class="abs mail-lines" style="top:365px"></div>
  <div class="abs mail-lines" style="top:412px"></div>

  <div class="abs schedule">SCHEDULE YOUR APPOINTMENT TODAY,</div>
  <div class="abs contact">Phone: 561-555-0143<br>Email: HarborviewSkin@mail.example</div>
</section>

</body>
</html>
```